Business Card and Word .doc header and footer required

I need a business card designed for my cybersecurity consulting company. Also required, is a header and footer to be ued for my word documents.
Attached is the Logo design, font and rgb used.

Industry/Entity Type

Cyber Security Consulting

Contact Information for Business Card

Name, Phone, email, website

Colors
0054AA
0677BA
7BADD7
CADEEF
E8F1F8

Requirements
Must have
• Sleek, modern

```html
<!DOCTYPE html>
<html lang="en">
<head>
<meta charset="UTF-8">
<title>Corvane Ridge Consulting – Business Card</title>
<link href="https://fonts.googleapis.com/css2?family=Oswald:wght@500&family=Montserrat:wght@600;700&family=Open+Sans:wght@400&display=swap" rel="stylesheet">
<style>
  :root {
    --blue-deep: #0054AA;
    --blue-main: #0677BA;
    --blue-soft: #7BADD7;
    --blue-pale: #CADEEF;
    --blue-mist: #E8F1F8;
    --ink: #14161c;
    --text-grey: #4a4d52;
    --card-white: #f4f4f2;
    --backdrop: #b9bec1;
  }
  * { margin: 0; padding: 0; box-sizing: border-box; }
  html, body {
    width: 1200px; height: 814px; overflow: hidden;
    background: var(--backdrop);
  }
  .stage { position: relative; width: 1200px; height: 814px; }

  .card {
    position: absolute;
    top: 258px;
    width: 520px; height: 298px;
    background: var(--card-white);
    border-bottom: 4px solid var(--blue-main);
    overflow: hidden;
  }
  .card--front { left: 60px; }
  .card--back  { left: 620px; }

  /* front side */
  .holder { position: absolute; left: 44px; top: 48px; }
  .holder__name {
    font-family: 'Oswald', sans-serif; font-weight: 500;
    font-size: 34px; line-height: 1; letter-spacing: 0.5px;
    color: var(--blue-main); text-transform: uppercase;
  }
  .holder__title {
    font-family: 'Montserrat', sans-serif; font-weight: 700;
    font-size: 13px; color: var(--ink); margin-top: 4px;
  }
  .contacts { list-style: none; position: absolute; left: 44px; top: 134px; }
  .contacts__item {
    display: flex; align-items: center; gap: 10px;
    font-family: 'Open Sans', sans-serif; font-size: 14px;
    color: var(--text-grey); height: 27px;
  }
  .contacts__icon { width: 18px; height: 18px; flex: none; }

  .stripe {
    position: absolute; top: 0; bottom: 0;
    width: 13px; background: var(--blue-main);
  }
  .stripe--first  { left: 340px; }
  .stripe--second { left: 368px; }

  /* back side */
  .brand {
    position: absolute; left: 0; right: 0; top: 0; bottom: 0;
    display: flex; align-items: center; justify-content: center; gap: 14px;
  }
  .brand__dot {
    width: 34px; height: 34px; border-radius: 50%;
    background: var(--blue-main); flex: none;
  }
  .brand__name {
    font-family: 'Montserrat', sans-serif; font-weight: 700;
    font-size: 22px; line-height: 1.2; letter-spacing: 1px;
    color: var(--ink); text-transform: uppercase;
  }
</style>
</head>
<body>
<main class="stage">

  <section class="card card--front" aria-label="Business card, front">
    <div class="holder">
      <h1 class="holder__name">Daniel Harper</h1>
      <p class="holder__title">President</p>
    </div>
    <ul class="contacts">
      <li class="contacts__item">
        <svg class="contacts__icon" viewBox="0 0 18 18" aria-hidden="true">
          <circle cx="9" cy="9" r="9" fill="var(--blue-main)"/>
          <path d="M6 4.5c.6-.3 1.1 0 1.4.6l.6 1.3c.2.5 0 .9-.4 1.2l-.4.3c.4 1 1.3 1.9 2.3 2.3l.3-.4c.3-.4.7-.6 1.2-.4l1.3.6c.6.3.9.8.6 1.4-.4.9-1.3 1.3-2.2 1.1C8.5 12 6 9.5 5.5 7.3c-.2-.9.1-2.4.5-2.8z" fill="#fff"/>
        </svg>
        369-555-0142
      </li>
      <li class="contacts__item">
        <svg class="contacts__icon" viewBox="0 0 18 18" aria-hidden="true">
          <circle cx="9" cy="9" r="9" fill="var(--blue-main)"/>
          <rect x="4.5" y="5.8" width="9" height="6.4" rx="0.8" fill="#fff"/>
          <path d="M4.8 6.2 9 9.4l4.2-3.2" fill="none" stroke="var(--blue-main)" stroke-width="1"/>
        </svg>
        daniel@corvaneridge.com
      </li>
      <li class="contacts__item">
        <svg class="contacts__icon" viewBox="0 0 18 18" aria-hidden="true">
          <circle cx="9" cy="9" r="9" fill="var(--blue-main)"/>
          <circle cx="9" cy="9" r="4.6" fill="none" stroke="#fff" stroke-width="1.2"/>
          <ellipse cx="9" cy="9" rx="2" ry="4.6" fill="none" stroke="#fff" stroke-width="1"/>
          <path d="M4.4 9h9.2" stroke="#fff" stroke-width="1"/>
        </svg>
        www.corvaneridge.com
      </li>
    </ul>
    <span class="stripe stripe--first" aria-hidden="true"></span>
    <span class="stripe stripe--second" aria-hidden="true"></span>
  </section>

  <section class="card card--back" aria-label="Business card, back">
    <div class="brand">
      <span class="brand__dot" aria-hidden="true"></span>
      <p class="brand__name">Corvane Ridge<br>Consulting</p>
    </div>
  </section>

</main>
</body>
</html>
```